Logo for civil excavation / rock production
Harrowby-Stenmark Holdings, LLC
Thanks everyone! Add tag line.. Civil Construction - Aggregate Production
Also - Cell phone most obvious and bold
Liking the shadow of logo

```html
<!DOCTYPE html>
<html lang="en">
<head>
<meta charset="utf-8">
<title>Harrowby-Stenmark Holdings, LLC – Business Card</title>
<link href="https://fonts.googleapis.com/css2?family=Arimo:wght@400;700&display=swap" rel="stylesheet">
<style>
  :root {
    --brand-blue: #2f6a9c;
    --brand-green: #98a75a;
    --ink-grey: #6d7378;
    --card-white: #fbfbfa;
    --backdrop: #e6e7e8;
    --on-blue: #ffffff;
  }
  * { margin: 0; padding: 0; box-sizing: border-box; }
  html, body { width: 1200px; height: 838px; overflow: hidden; }
  body {
    background: var(--backdrop);
    font-family: "Arimo", Arial, sans-serif;
    position: relative;
  }
  .card {
    position: absolute;
    top: 264px;
    width: 540px;
    height: 309px;
    background: var(--card-white);
    border-radius: 3px;
    box-shadow: 0 6px 18px rgba(0,0,0,0.18);
    overflow: hidden;
  }
  .card--front { left: 40px; }
  .card--back { left: 620px; display: flex; align-items: center; justify-content: center; }

  .card__wave { position: absolute; inset: 0; width: 100%; height: 100%; }

  .brand { position: absolute; left: 36px; top: 34px; }
  .company-name {
    color: var(--brand-blue);
    font-weight: 700;
    font-size: 19px;
    letter-spacing: 1.5px;
    line-height: 1.25;
    text-transform: uppercase;
  }
  .company-name__mark {
    display: inline-block;
    width: 14px; height: 14px;
    border-radius: 50%;
    background: var(--brand-blue);
    margin-right: 8px;
    vertical-align: -1px;
  }
  .tagline {
    margin-top: 5px;
    color: var(--ink-grey);
    font-size: 9.5px;
    letter-spacing: 1px;
    text-transform: uppercase;
  }
  .person { position: absolute; left: 36px; top: 114px; }
  .person__name { color: var(--brand-blue); font-size: 17px; }
  .person__role { color: var(--ink-grey); font-size: 10px; margin-top: 3px; }

  .contact {
    position: absolute;
    right: 28px;
    top: 178px;
    text-align: right;
    color: var(--on-blue);
    font-size: 14px;
    line-height: 1.45;
  }
  .contact__city { margin-bottom: 6px; }
  .contact__cell { font-weight: 700; }

  .back-brand { text-align: center; }
  .back-name {
    color: var(--brand-blue);
    font-weight: 700;
    font-size: 26px;
    letter-spacing: 2px;
    text-transform: uppercase;
    line-height: 1.3;
  }
  .back-name__mark {
    display: block;
    width: 64px; height: 64px;
    margin: 0 auto 18px;
    border-radius: 50%;
    background: var(--brand-blue);
  }
  .back-tagline {
    margin-top: 12px;
    color: var(--ink-grey);
    font-size: 12px;
    letter-spacing: 1.5px;
    text-transform: uppercase;
  }
</style>
</head>
<body>
  <section class="card card--front">
    <svg class="card__wave" viewBox="0 0 540 309" preserveAspectRatio="none" aria-hidden="true">
      <path d="M0 192 C150 158 330 176 540 128" fill="none" stroke="var(--brand-blue)" stroke-width="2"/>
      <path d="M0 202 C150 168 330 186 540 138" fill="none" stroke="var(--brand-green)" stroke-width="3"/>
      <path d="M0 215 C150 180 330 198 540 150 L540 309 L0 309 Z" fill="var(--brand-blue)"/>
    </svg>
    <div class="brand">
      <div class="company-name"><span class="company-name__mark"></span>Harrowby-Stenmark<br>Holdings, LLC</div>
      <div class="tagline">Civil Construction - Aggregate Production</div>
    </div>
    <div class="person">
      <div class="person__name">Conrad Hallwey</div>
      <div class="person__role">Managing Member</div>
    </div>
    <div class="contact">
      <div class="contact__city">Millbrook, ND</div>
      <div>Phone: (701) 555-0142</div>
      <div class="contact__cell">Cell: (509) 555-0187</div>
      <div>Fax: (509) 555-0163</div>
      <div>Email: conrad@harrowbyinc.com</div>
    </div>
  </section>

  <section class="card card--back">
    <div class="back-brand">
      <div class="back-name"><span class="back-name__mark"></span>Harrowby-Stenmark<br>Holdings, LLC</div>
      <div class="back-tagline">Civil Construction - Aggregate Production</div>
    </div>
  </section>
</body>
</html>
```